Looking for business card/letterhead/email signature

Take existing logo and create full design suite of collateral

Contact Information for Business Card

Use mock details that can be edited by us

Font styles to use
Sans Serif

```html
<!DOCTYPE html>
<html lang="en">
<head>
<meta charset="utf-8">
<title>Harlow Digital — Stationery Suite</title>
<link href="https://fonts.googleapis.com/css2?family=Lato:wght@400;700&display=swap" rel="stylesheet">
<style>
:root{
  --bg:#d9e1df;
  --paper:#ffffff;
  --brand-blue:#0a3fbf;
  --brand-red:#e8195a;
  --brand-orange:#f47c20;
  --brand-sky:#5bc8f0;
  --ink:#3a3f44;
  --ink-soft:#5a6066;
  --rule:#8a9096;
}
*{margin:0;padding:0;box-sizing:border-box}
html,body{width:1200px;height:1200px;overflow:hidden;background:var(--bg)}
body{position:relative;font-family:"Lato",sans-serif;color:var(--ink)}
.sheet{position:absolute;background:var(--paper);box-shadow:0 6px 10px rgba(0,0,0,.18)}
.abs{position:absolute}
.brand{font-family:"Lato",sans-serif;font-weight:700;color:var(--brand-blue);white-space:nowrap;display:flex;align-items:center}

/* Letterhead */
.letterhead{left:249px;top:96px;width:520px;height:736px}
.letterhead .top-band{left:0;top:0;width:100%;height:8px;background:var(--brand-blue)}
.letterhead .brand{left:0;width:100%;top:42px;justify-content:center;font-size:26px}
.letterhead .address{left:0;width:100%;top:99px;text-align:center;font-size:8.5px;color:var(--ink)}
.letterhead .salutation{left:59px;top:190px;font-size:8.5px}
.letterhead .body{left:59px;top:230px;width:403px;font-size:8.3px;line-height:10.4px;text-align:justify;color:var(--ink-soft)}
.letterhead .body p{margin-bottom:17px}
.letterhead .body p.lead{font-weight:700;color:#3a4a5c;font-size:8.6px;line-height:10.8px;margin-bottom:14px}
.letterhead .signature{left:62px;top:608px;width:80px;height:22px;background:linear-gradient(90deg,#eceef0,#f6f7f8);border-bottom:1px solid var(--ink)}
.letterhead .contacts{left:0;width:100%;top:694px;display:flex;justify-content:center;gap:32px;font-size:5.5px;color:var(--ink-soft)}
.letterhead .contacts div{display:flex;flex-direction:column;align-items:center;gap:3px}
.letterhead .bottom-band{left:0;bottom:0;width:100%;height:5px;display:flex}
.seg-red{background:var(--brand-red)}.seg-orange{background:var(--brand-orange)}.seg-sky{background:var(--brand-sky)}.seg-blue{background:var(--brand-blue)}

/* Business cards */
.card{left:742px;width:254px;height:145px}
.card-front{top:426px}
.card-back{top:596px}
.stripe{top:0;height:100%;display:flex;flex-direction:column}
.stripe div{flex:1}
.card-front .stripe{left:228px;width:4px}
.card-front .panel{left:232px;top:0;width:22px;height:100%;background:var(--brand-blue)}
.card-front .panel span{position:absolute;left:50%;top:50%;transform:translate(-50%,-50%) rotate(-90deg);color:#fff;font-size:5px;white-space:nowrap}
.card-front .brand{left:0;width:228px;top:58px;justify-content:center;font-size:24px}
.card-back .stripe{left:189px;width:5px}
.card-back .panel{left:194px;top:0;width:60px;height:100%;background:var(--brand-blue)}
.card-back .panel .brand{position:absolute;left:50%;top:50%;transform:translate(-50%,-50%) rotate(-90deg);color:#fff;font-size:18px}
.card-back .name{left:24px;top:22px;font-size:10px;font-weight:700;color:#1f2328}
.card-back .role{left:24px;top:34px;font-size:6px;color:var(--brand-blue)}
.card-back .info{left:24px;top:76px;font-size:5.2px;line-height:9.3px;color:var(--ink)}
.card-back .info div{display:flex;align-items:center;gap:5px}
.card-back .info .addr{margin-top:6px;align-items:flex-start;line-height:7px}
.ico{flex:none}

/* Email signature */
.email{left:301px;top:902px;width:501px;height:192px}
.email .brand{left:40px;top:30px;font-size:18px}
.email .divider{top:28px;width:1px;height:30px;background:var(--rule)}
.email .photo{left:177px;top:22px;width:36px;height:36px;border-radius:50%;border:3px solid var(--brand-blue);background:radial-gradient(circle at 50% 40%,#c9a48c,#5a6a7a)}
.email .person{left:219px;top:30px}
.email .person .full{font-size:14px;color:#2a2f35;line-height:15px}
.email .person .title{font-size:9.5px;color:var(--ink);margin-left:2px}
.email .place{left:327px;top:30px;font-size:9.5px;line-height:14px;color:var(--ink)}
.email .bar{left:40px;top:64px;width:409px;height:3px;display:flex}
.email .bar div{flex:1}
.email .links{left:40px;top:76px;width:409px;display:flex;gap:18px;font-size:9.5px;color:var(--ink)}
.email .links b{font-weight:400;color:var(--brand-blue)}
.email .rule{left:40px;top:96px;width:410px;height:1px;background:var(--rule)}
.email .note{left:40px;top:107px;width:412px;font-size:6px;line-height:8.6px;color:var(--ink-soft);text-align:justify}
.email .copy{left:40px;top:151px;font-size:6.4px;color:var(--ink-soft)}
</style>
</head>
<body>

<section class="sheet letterhead">
  <div class="abs top-band"></div>
  <div class="abs brand"><span>harlow digital</span></div>
  <p class="abs address">Brookfield House, Mill Lane, Ashcombe, Surrey KT19 4LP</p>
  <p class="abs salutation">Dear, Mr_________</p>
  <div class="abs body">
    <p>Lorem Ipsum is simply dummy text of the printing and typesetting industry. Lorem Ipsum has been the industry's standard dummy text ever since the1500s,when an unknown printer took a galley of type and scrambled it to make a type specimen book. It has survived not only five centuries, but also the leap into electronic typesetting, remaining essentially unchanged. It was popularised in the 1960s with the release of Letraset sheets containing Lorem Ipsum passages,and more recently with desktop publishing software like Aldus PageMaker including versions of Lorem Ipsum.</p>
    <p>Lorem Ipsum is simply dummy text of the printing and typesetting industry. Lorem Ipsum has been the industry's standard dummy text ever since the1500s,when an unknown printer took a galley of type and scrambled it to make a type specimen book. It has survived not only five centuries, but also the leap into electronic typesetting, remaining essentially unchanged. It was popularised in the 1960s with the release of Letraset sheets containing Lorem Ipsum passages,and more recently with desktop publishing software like Aldus PageMaker including versions of Lorem Ipsum.</p>
    <p class="lead">Lorem Ipsum is simply dummy text of the printing and typesetting industry. Lorem Ipsum has been the industry's standard dummy text ever since the1500s,when an unknown printer took a galley of type and scrambled it to make a type specimen book.</p>
    <p>Lorem Ipsum is simply dummy text of the printing and typesetting industry. Lorem Ipsum has been the industry's standard dummy text ever since the1500s,when an unknown printer took a galley of type and scrambled it to make a type specimen book. It has survived not only five centuries, but also the leap into electronic typesetting, remaining essentially unchanged. It was popularised in the 1960s with the release of Letraset sheets containing Lorem Ipsum passages,and more recently with desktop publishing software like Aldus PageMaker including versions of Lorem Ipsum.</p>
    <p>Lorem Ipsum is simply dummy text of the printing and typesetting industry. Lorem Ipsum has been the industry's standard dummy text ever since the1500s,when an unknown printer took a galley of type and scrambled it to make a type specimen book.</p>
  </div>
  <div class="abs signature" role="img" aria-label="Handwritten signature"></div>
  <div class="abs contacts">
    <div><svg class="ico" width="7" height="7" viewBox="0 0 10 10"><path d="M2 1l2 2-1 1.5c.6 1.3 1.3 2 2.5 2.5L7 6l2 2-1.5 1.5C4.5 9 1 5.5.5 2.5z" fill="var(--brand-red)"/></svg>+02-987 654 32</div>
    <div><svg class="ico" width="8" height="7" viewBox="0 0 10 8"><rect width="10" height="8" fill="var(--brand-red)"/><path d="M0 0l5 4 5-4" stroke="#fff" fill="none"/></svg>info@harlowdigital.com</div>
    <div><svg class="ico" width="7" height="7" viewBox="0 0 10 10"><circle cx="5" cy="5" r="4.3" fill="none" stroke="var(--brand-red)" stroke-width="1.2"/><path d="M.7 5h8.6M5 .7v8.6M5 .7c-2.5 2.5-2.5 6 0 8.6M5 .7c2.5 2.5 2.5 6 0 8.6" stroke="var(--brand-red)" fill="none" stroke-width=".8"/></svg>www.harlowdigital.com</div>
  </div>
  <div class="abs bottom-band"><div class="seg-red" style="width:150px"></div><div class="seg-orange" style="width:226px"></div><div class="seg-sky" style="flex:1"></div></div>
</section>

<section class="sheet card card-front">
  <div class="abs brand"><span>harlow digital</span></div>
  <div class="abs stripe"><div class="seg-red"></div><div class="seg-orange"></div><div class="seg-sky"></div></div>
  <div class="abs panel"><span>www.harlowdigital.com</span></div>
</section>

<section class="sheet card card-back">
  <p class="abs name">Simon Ardenly</p>
  <p class="abs role">Director</p>
  <div class="abs info">
    <div><svg class="ico" width="5" height="5" viewBox="0 0 10 10"><path d="M2 1l2 2-1 1.5c.6 1.3 1.3 2 2.5 2.5L7 6l2 2-1.5 1.5C4.5 9 1 5.5.5 2.5z" fill="var(--brand-red)"/></svg>+02-987 654 32</div>
    <div><svg class="ico" width="5" height="4" viewBox="0 0 10 8"><rect width="10" height="8" fill="var(--brand-red)"/></svg>info@harlowdigital.com</div>
    <div><svg class="ico" width="5" height="5" viewBox="0 0 10 10"><circle cx="5" cy="5" r="4" fill="none" stroke="var(--brand-red)" stroke-width="1.5"/></svg>www.harlowdigital.com</div>
    <div class="addr"><svg class="ico" width="5" height="6" viewBox="0 0 10 12"><path d="M5 12S0 6.5 0 4a5 5 0 0110 0c0 2.5-5 8-5 8z" fill="var(--brand-red)"/></svg><span>Brookfield House, Mill Lane, Ashcombe,<br>Surrey KT19 4LP</span></div>
  </div>
  <div class="abs stripe"><div class="seg-red"></div><div class="seg-orange"></div><div class="seg-sky"></div></div>
  <div class="abs panel"><div class="brand"><span>harlow</span></div></div>
</section>

<section class="sheet email">
  <div class="abs brand"><span>harlow</span></div>
  <div class="abs divider" style="left:151px"></div>
  <div class="abs photo" role="img" aria-label="Portrait photo of the sender"></div>
  <div class="abs person"><p class="full">Your Name</p><p class="title">Designation</p></div>
  <div class="abs divider" style="left:312px"></div>
  <p class="abs place">12 Palmview Rd. Honolulu,<br>HI 96815</p>
  <div class="abs bar"><div class="seg-blue"></div><div class="seg-red"></div><div class="seg-sky"></div><div class="seg-orange"></div></div>
  <div class="abs links"><span><b>Phone :</b> +02-987 654 32</span><span><b>E-Mail :</b>info@harlowdigital.com</span><span><b>Website :</b> www.harlowdigital.com</span></div>
  <div class="abs rule"></div>
  <p class="abs note">Lorem Ipsum is simply dummy text of the printing and typesetting industry. Lorem Ipsum has been the industry's standard dummy text ever since the 1500s, when an unknown printer took a galley of type and scrambled it to make a type specimen book. It has survived not only five centuries, but also the leap into electronic typesetting, remaining essentially unchanged.</p>
  <p class="abs copy">© 2018 harlow digital . All Rights Reserved.</p>
</section>

</body>
</html>
```